Broschüre für unsere Firma
Zielgruppe
Wäscherei Kranzbeck / Textilservice
Geschäftskunden
Logos etc. In OneDrive/ Dropbox
https://ablage-beispiel.de/f/s!XkrTmWq7PzvoNeFgHsYa4Lc92_p
Wir wollen gerne eine 4 seitige Broschüre erstellen lassen, um unsere Firma vorzustellen.
Insbesondere der Service
Berufsbekleidung
Hygiene Gardienenwäsche Service
Hotelmietwäsche
Mitbewerb
http://www.wäscherei-gollwitz.de/index.php/ct-menu-item-17/ct-menu-item-25
http://www.tuch-morgen.ch/download
Im Anhang finden Sie Bilder Logo und Flyers welche wir mal selbst gemacht haben!
Datein sind im OneDrive
Aufgabenstellung

```html
<!DOCTYPE html>
<html lang="de">
<head>
<meta charset="utf-8">
<title>Wäscherei Kranzbeck – Broschüre</title>
<link rel="stylesheet" href="https://fonts.googleapis.com/css2?family=Ubuntu:wght@300;400;500;700&family=Cabin:ital,wght@0,400;0,600;1,600&display=swap">
<style>
:root{
  --backdrop:#464646;
  --green:#7ab92f;
  --green-light:#a6d17b;
  --blue:#2f3d91;
  --blue-soft:#6b73b4;
  --white:#ffffff;
  --ink:#2b2b2b;
  --font-head:"Ubuntu",sans-serif;
  --font-body:"Cabin",sans-serif;
}
*{box-sizing:border-box;margin:0;padding:0}
html,body{width:763px;height:1200px;overflow:hidden;background:var(--backdrop)}
.stage{position:relative;width:1500px;height:2359px;transform:scale(0.50867);transform-origin:0 0}
.sheet-label{position:absolute;font-family:var(--font-head);font-weight:300;font-size:28px;letter-spacing:1px;color:var(--white)}
.spread{position:absolute;left:54px;width:1390px;height:981px;background:var(--white);overflow:hidden}
.spread--outside{top:132px}
.spread--inside{top:1286px}
.spread svg.shapes{position:absolute;inset:0;width:100%;height:100%}
.abs{position:absolute}

/* outside: contact */
.contact-title{left:150px;top:556px;width:394px;text-align:center;font-family:var(--font-head);font-weight:500;font-size:19px;letter-spacing:.5px;color:var(--blue)}
.contact-col{font-family:var(--font-body);font-size:12.5px;line-height:17px;color:var(--white)}
.contact-col strong{display:block;font-weight:600;margin-bottom:6px}
.contact-col p{margin-bottom:6px}
.contact-col--address{left:180px;top:622px;width:166px;text-align:center}
.contact-col--hours{left:382px;top:622px;width:160px}
.contact-divider{left:353px;top:623px;width:1.5px;height:123px;background:var(--white)}

.brand{left:1116px;top:378px;display:flex;align-items:center;gap:10px}
.brand-dot{width:34px;height:34px;border-radius:50%;background:var(--green)}
.brand-name{font-family:var(--font-head);font-weight:700;font-size:22px;color:var(--blue);white-space:nowrap}

/* inside */
.headline{left:44px;top:38px;font-family:var(--font-head);font-weight:700;font-size:34px;line-height:46px;letter-spacing:.5px;color:var(--blue)}
.intro-box{left:341px;top:192px;width:272px;height:369px;background:var(--blue);color:var(--white);font-family:var(--font-body);font-size:14.5px;line-height:20px;text-align:center;padding:25px 10px 0}
.intro-box p{margin-bottom:16px}
.intro-box em{font-style:normal;font-weight:600;color:var(--green);letter-spacing:1px;text-transform:uppercase}

.service{width:260px}
.service h2{font-family:var(--font-head);font-weight:500;font-size:19px;letter-spacing:.5px;color:var(--blue);padding-bottom:3px;border-bottom:1.5px solid var(--green);width:208px;margin-bottom:14px}
.service .copy{margin-left:23px;width:218px;font-family:var(--font-body);font-size:10.5px;line-height:15.2px;color:var(--ink)}
.service .copy p{margin-bottom:15px}
.service .copy b{font-weight:600;font-style:italic}
.service--work{left:740px;top:152px}
.service--hotel{left:1063px;top:152px}
.service--curtain{left:740px;top:489px}
.service--more{left:1063px;top:489px}
.service-list{list-style:none;margin-left:23px;font-family:var(--font-body);font-size:10.5px;line-height:15.2px;color:var(--ink)}
.service-list li{display:flex;align-items:center;gap:8px}
.service-list svg{width:11px;height:10px;flex:none}
</style>
</head>
<body>
<div class="stage">

  <div class="sheet-label" style="left:81px;top:74px">AUSSEN</div>

  <section class="spread spread--outside">
    <svg class="shapes" viewBox="0 0 1390 981" aria-hidden="true">
      <!-- left panel -->
      <polygon points="0,0 8,0 694,480 694,790 0,968" fill="var(--green)"/>
      <polygon points="24,0 70,0 694,482" fill="var(--blue)"/>
      <polygon points="694,794 0,972 0,981 62,981" fill="var(--blue)"/>
      <g fill="var(--green-light)">
        <circle cx="48" cy="268" r="27"/>
        <circle cx="183" cy="291" r="23"/>
        <circle cx="124" cy="361" r="26"/>
        <circle cx="257" cy="353" r="18"/>
        <circle cx="375" cy="402" r="23"/>
        <circle cx="0" cy="396" r="48"/>
        <circle cx="140" cy="843" r="37"/>
        <circle cx="245" cy="854" r="14"/>
        <circle cx="56" cy="901" r="25"/>
      </g>
      <!-- right panel -->
      <polygon points="694,0 1378,0 694,480" fill="var(--blue)"/>
      <polygon points="1390,8 1390,50 694,482" fill="var(--green)"/>
      <polygon points="694,794 1390,981 694,981" fill="var(--blue)"/>
      <polygon points="694,790 1390,935 1390,978" fill="var(--green)"/>
      <!-- certificates -->
      <rect x="736" y="855" width="62" height="104" rx="4" fill="#1f8a3c" stroke="var(--white)" stroke-width="2"/>
      <circle cx="852" cy="924" r="34" fill="#1f8a3c" stroke="var(--white)" stroke-width="2"/>
    </svg>

    <div class="abs" role="img" aria-label="Foto: Hand legt eine graue Hose auf dem Bügeltisch zurecht" style="left:694px;top:480px;width:235px;height:155px;background:linear-gradient(160deg,#c9c7c2,#7c7a74 60%,#3d6fb8)"></div>
    <div class="abs" role="img" aria-label="Foto: weiße Hemden auf Bügeln" style="left:694px;top:635px;width:235px;height:155px;background:linear-gradient(120deg,#f1eee8,#d9d4cc 55%,#b7b1a8)"></div>
    <div class="abs" role="img" aria-label="Foto: Mitarbeiterin kontrolliert verpackte Wäsche im Betrieb" style="left:929px;top:480px;width:235px;height:310px;background:linear-gradient(110deg,#e8e4e2,#e3b7c2 45%,#364f8a 80%,#2d3b6a)"></div>
    <div class="abs" role="img" aria-label="Foto: blaues Hemd in Schutzfolie" style="left:1164px;top:480px;width:226px;height:155px;background:linear-gradient(140deg,#e7e9ee,#4a62a0 55%,#2c3f78)"></div>
    <div class="abs" role="img" aria-label="Foto: kariertes Hemd zwischen hellen Kitteln" style="left:1164px;top:635px;width:226px;height:155px;background:linear-gradient(120deg,#f3ebe8,#d9cfcc 45%,#8e3a45 70%,#3d3f6c)"></div>

    <h2 class="abs contact-title">SO ERREICHEN SIE UNS</h2>
    <div class="abs contact-col contact-col--address">
      <strong>Kontakt</strong>
      <p>Lindenhofer Straße 12<br>D-58812 Eichenrode</p>
      <p>mail@kranzbeck.info</p>
      <p>Tel. +49 (0) 2391 55870<br>Fax. +49 (0) 2391 55871</p>
    </div>
    <div class="abs contact-divider"></div>
    <div class="abs contact-col contact-col--hours">
      <strong>Öffnungszeiten</strong>
      <p>Montag – Freitag<br>08:00 – 17:00 Uhr</p>
    </div>

    <div class="abs brand">
      <span class="brand-dot"></span>
      <span class="brand-name">Wäscherei Kranzbeck</span>
    </div>
  </section>

  <div class="sheet-label" style="left:79px;top:1228px">INNEN</div>

  <section class="spread spread--inside">
    <div class="abs" role="img" aria-label="Foto: Mitarbeiterin prüft Wäsche in Schutzfolie in der Wäscherei" style="left:0;top:90px;width:696px;height:880px;background:linear-gradient(100deg,#eceae6 0%,#e6c3cc 30%,#d9aab8 45%,#c9ccd6 62%,#3a4f86 82%,#26325e 100%)"></div>
    <svg class="shapes" viewBox="0 0 1390 981" aria-hidden="true">
      <polygon points="0,0 1272,0 0,192" fill="var(--green)"/>
      <polygon points="1392,0 1392,98 696,100" fill="var(--white)" opacity="0"/>
      <polygon points="696,104 1390,12 1390,981 696,981" fill="var(--white)"/>
      <polygon points="1290,0 1390,0 1390,12 0,192 0,190" fill="var(--blue)"/>
      <polygon points="0,981 0,968 1390,789 1390,800 60,981" fill="var(--green)"/>
      <polygon points="430,981 1390,806 1390,981" fill="var(--blue)"/>
    </svg>

    <h1 class="abs headline">WIR BIETEN<br>IHNEN…</h1>

    <div class="abs intro-box">
      <p>Wir sind ein<br><em>hygienezertifizierter Wäschereibetrieb</em><br>mit viel Erfahrung &amp; Tradition.</p>
      <p>Ihre Zufriedenheit steht<br>bei uns an erster Stelle.</p>
      <p>Ihre Wäsche wird nicht nur<br><em>strahlend sauber,</em><br>sondern auch ökologisch und<br>ökonomisch einwandfrei behandelt.</p>
      <p><em>Qualifizierte Mitarbeiter</em><br>und <em>modernste Technik</em><br>gewährleisten ein gleichbleibend<br>hohes Niveau unserer Arbeit.</p>
    </div>

    <article class="abs service service--work">
      <h2>BERUFSBEKLEIDUNG</h2>
      <div class="copy">
        <p>Dies ist ein <b>Typoblindtext</b>. An ihm kann man sehen, ob alle Buchstaben da sind und wie sie aussehen. Manchmal benutzt man Worte wie Hamburgefonts, Rafgenduks oder Handgloves, um Schriften zu testen.</p>
        <p>Manchmal Sätze, die alle Buchstaben des Alphabets enthalten - man nennt diese Sätze <b>»Pangrams«</b>. Sehr bekannt ist dieser: The quick brown fox jumps over the lazy old dog. Oft werden in Typoblindtexte auch fremdsprachige Satzteile eingebaut (AVAIL® and Wefox™ are testing aussi la Kerning), um die <b>Wirkung in anderen Sprachen</b> zu testen. In Lateinisch sieht zum Beispiel fast jede Schrift gut aus.</p>
      </div>
    </article>

    <article class="abs service service--hotel">
      <h2>HOTELWÄSCHE</h2>
      <div class="copy">
        <p>Dies ist ein <b>Typoblindtext</b>. An ihm kann man sehen, ob alle Buchstaben da sind und wie sie aussehen. Manchmal benutzt man Worte wie Hamburgefonts, Rafgenduks oder Handgloves, um Schriften zu testen.</p>
        <p>Manchmal Sätze, die alle Buchstaben des Alphabets enthalten - man nennt diese Sätze <b>»Pangrams«</b>. Sehr bekannt ist dieser: The quick brown fox jumps over the lazy old dog. Oft werden in Typoblindtexte auch fremdsprachige Satzteile eingebaut (AVAIL® and Wefox™ are testing aussi la Kerning), um die <b>Wirkung in anderen Sprachen</b> zu testen. In Lateinisch sieht zum Beispiel fast jede Schrift gut aus.</p>
      </div>
    </article>

    <article class="abs service service--curtain">
      <h2>GARDINENWÄSCHE</h2>
      <div class="copy">
        <p>Dies ist ein <b>Typoblindtext</b>. An ihm kann man sehen, ob alle Buchstaben da sind und wie sie aussehen. Manchmal benutzt man Worte wie Hamburgefonts, Rafgenduks oder Handgloves, um Schriften zu testen.</p>
        <p>Manchmal Sätze, die alle Buchstaben des Alphabets enthalten - man nennt diese Sätze <b>»Pangrams«</b>. Sehr bekannt ist dieser: The quick brown fox jumps over the lazy old dog. Oft werden in Typoblindtexte auch fremdsprachige Satzteile eingebaut (AVAIL® and Wefox™ are testing aussi la Kerning), um die <b>Wirkung in anderen Sprachen</b> zu testen. In Lateinisch sieht zum Beispiel fast jede Schrift gut aus.</p>
      </div>
    </article>

    <article class="abs service service--more">
      <h2>WEITERE SERVICES</h2>
      <ul class="service-list">
        <li><svg viewBox="0 0 11 10"><path d="M1 5.5 4 8.5 10 1" fill="none" stroke="var(--green)" stroke-width="1.6"/></svg>Altenheimwäsche</li>
        <li><svg viewBox="0 0 11 10"><path d="M1 5.5 4 8.5 10 1" fill="none" stroke="var(--green)" stroke-width="1.6"/></svg>Flammschutzausrüstung</li>
        <li><svg viewBox="0 0 11 10"><path d="M1 5.5 4 8.5 10 1" fill="none" stroke="var(--green)" stroke-width="1.6"/></svg>Gastronomiewäsche</li>
        <li><svg viewBox="0 0 11 10"><path d="M1 5.5 4 8.5 10 1" fill="none" stroke="var(--green)" stroke-width="1.6"/></svg>Haushaltswäsche</li>
        <li><svg viewBox="0 0 11 10"><path d="M1 5.5 4 8.5 10 1" fill="none" stroke="var(--green)" stroke-width="1.6"/></svg>Imprägnierservice</li>
        <li><svg viewBox="0 0 11 10"><path d="M1 5.5 4 8.5 10 1" fill="none" stroke="var(--green)" stroke-width="1.6"/></svg>Kittelservice</li>
        <li><svg viewBox="0 0 11 10"><path d="M1 5.5 4 8.5 10 1" fill="none" stroke="var(--green)" stroke-width="1.6"/></svg>Lamellenreinigung</li>
        <li><svg viewBox="0 0 11 10"><path d="M1 5.5 4 8.5 10 1" fill="none" stroke="var(--green)" stroke-width="1.6"/></svg>Mangelwäsche</li>
        <li><svg viewBox="0 0 11 10"><path d="M1 5.5 4 8.5 10 1" fill="none" stroke="var(--green)" stroke-width="1.6"/></svg>Oberbetten / Kissen / Wasserbetten</li>
        <li><svg viewBox="0 0 11 10"><path d="M1 5.5 4 8.5 10 1" fill="none" stroke="var(--green)" stroke-width="1.6"/></svg>Oberhemden</li>
        <li><svg viewBox="0 0 11 10"><path d="M1 5.5 4 8.5 10 1" fill="none" stroke="var(--green)" stroke-width="1.6"/></svg>Pferdedecken</li>
        <li><svg viewBox="0 0 11 10"><path d="M1 5.5 4 8.5 10 1" fill="none" stroke="var(--green)" stroke-width="1.6"/></svg>Teppichreinigung</li>
        <li><svg viewBox="0 0 11 10"><path d="M1 5.5 4 8.5 10 1" fill="none" stroke="var(--green)" stroke-width="1.6"/></svg>Textilreinigung</li>
        <li><svg viewBox="0 0 11 10"><path d="M1 5.5 4 8.5 10 1" fill="none" stroke="var(--green)" stroke-width="1.6"/></svg>Wascheraumhygiene</li>
        <li><svg viewBox="0 0 11 10"><path d="M1 5.5 4 8.5 10 1" fill="none" stroke="var(--green)" stroke-width="1.6"/></svg>Hol- und Bringservice</li>
      </ul>
    </article>
  </section>

</div>
</body>
</html>
```